Design Workout/Fitness Mobile App

Create a design for a mobile workout out a mobile app called Brisko Routine. This workout app is very similar to Tenfold Stretch. Please download or search for the Tenfold Stretch in the Appvane Shelf to get an idea, I will also include a link below.

App Description: http://lnkvex.example/q7Rt2aW

The main difference between Brisko Routine and Tenfold Stretch is that Brisko Routines are 8 Minutes instead of Tenfold and Brisko Routine are created/demonstrated by a real human being instead of an animated video.
Please read the referenced Quillo Sheet and install or go through the Tenfold app. I am open to any design color. The app is targetted at people who need a quick workout but do not have a lot of time

Example (Tenfold Stretch): http://lnkvex.example/m4Kd9Ye

Target Market(s)

Busy working adults

Industry/Entity Type

Fitness

Colors

Designer to choose colors to be used in the design.

Requirements
Must have
• This design is for at least three screens
• The main screen showing a list of the types of exercises such as lower body, abs, etc
• The workout screen showing the video
• A calendar showing the number of days user worked.
Nice to have
• Make the designs close to the tenfold stretch with different look and feel

```html
<!DOCTYPE html>
<html lang="en">
<head>
<meta charset="utf-8">
<title>Brisko Routine – App Screens</title>
<link rel="stylesheet" href="https://fonts.googleapis.com/css2?family=Mulish:wght@400;600;700;800&display=swap">
<style>
  :root {
    --stage: #141414;
    --chrome: #2c3136;
    --chrome-deep: #23272b;
    --accent: #f6c21c;
    --paper: #ffffff;
    --ink: #2a2a2a;
    --ink-soft: #5a5a5a;
    --muted: #9a9a9a;
    --rule: #e6e6e6;
  }
  * { box-sizing: border-box; margin: 0; padding: 0; }
  html, body { width: 1200px; height: 1200px; overflow: hidden; }
  body {
    background: var(--stage);
    font-family: "Mulish", Arial, sans-serif;
    position: relative;
  }
  .brand-title {
    position: absolute; top: 232px; left: 0; width: 1200px;
    text-align: center; color: var(--paper);
    font-weight: 800; font-size: 62px; letter-spacing: 2px; text-transform: uppercase;
  }
  .screen {
    position: absolute; top: 442px; width: 298px; height: 648px;
    border-radius: 28px; overflow: hidden; background: var(--paper);
  }
  .screen--splash { left: 74px; background: var(--chrome); }
  .screen--dashboard { left: 460px; }
  .screen--workout { left: 838px; }

  .status-bar {
    position: absolute; top: 0; left: 0; right: 0; height: 34px;
    display: flex; align-items: center; justify-content: space-between;
    padding: 6px 22px 0 24px; color: var(--paper); font-size: 13px; font-weight: 600;
  }
  .status-icons { display: flex; gap: 4px; align-items: center; }

  .splash-photo {
    position: absolute; left: 0; top: 100px; width: 298px; height: 548px;
    background: radial-gradient(ellipse at 50% 30%, #4a4f54 0%, #3a3f44 45%, var(--chrome) 80%);
  }
  .splash-name {
    position: absolute; top: 300px; left: 0; width: 298px; text-align: center;
    color: var(--paper); font-weight: 800; font-size: 30px; line-height: 1.05; text-transform: uppercase;
  }

  .app-header {
    height: 83px; background: var(--chrome); position: relative;
  }
  .app-header__title {
    position: absolute; bottom: 10px; left: 0; right: 0; text-align: center;
    color: var(--paper); font-size: 17px; font-weight: 400;
  }
  .app-header__icon { position: absolute; bottom: 12px; }

  .tabs { display: flex; height: 40px; border-bottom: 1px solid var(--rule); }
  .tab { flex: 1; text-align: center; padding-top: 9px; font-size: 15px; color: var(--muted); }
  .tab--active { color: var(--ink); font-weight: 700; position: relative; }
  .tab--active::after {
    content: ""; position: absolute; bottom: 5px; left: 30px; right: 30px; height: 2px; background: var(--accent);
  }

  .card-list { padding: 2px 3px 0; display: flex; flex-direction: column; gap: 3px; }
  .workout-card { position: relative; height: 151px; }
  .workout-card__photo { position: absolute; inset: 0; }
  .workout-card__caption {
    position: absolute; left: 0; right: 0; bottom: 0; height: 54px;
    background: rgba(40, 44, 48, 0.72); padding: 10px 18px 0;
  }
  .workout-card__title { color: var(--accent); font-weight: 800; font-size: 15px; }
  .workout-card__desc { color: var(--paper); font-size: 8.5px; font-weight: 700; margin-top: 2px; white-space: nowrap; overflow: hidden; text-overflow: ellipsis; }
  .workout-card--short { height: 60px; }

  .exercise-title { font-size: 14px; font-weight: 700; color: var(--ink); padding: 12px 12px 9px; letter-spacing: 0.3px; }
  .exercise-video { position: relative; height: 151px; margin: 0 3px; }
  .exercise-video__play { position: absolute; left: 50%; top: 50%; transform: translate(-50%, -50%); }
  .exercise-text { font-size: 11px; color: var(--ink-soft); line-height: 1.2; padding: 14px 12px 0; }
  .exercise-text + .exercise-text { padding-top: 13px; }
  .fab {
    position: absolute; right: 10px; top: 562px; width: 56px; height: 56px; border-radius: 50%;
    background: var(--accent); display: flex; align-items: center; justify-content: center;
    box-shadow: 0 3px 8px rgba(0,0,0,.25);
  }
</style>
</head>
<body>

<h1 class="brand-title">Brisko Routine</h1>

<!-- Splash screen -->
<section class="screen screen--splash">
  <div class="splash-photo" role="img" aria-label="Faded photo of a smiling trainer holding a dumbbell"></div>
  <div class="status-bar">
    <span>9:41</span>
    <span class="status-icons">
      <svg width="16" height="10" viewBox="0 0 16 10"><rect x="0" y="7" width="3" height="3" fill="#fff"/><rect x="4" y="5" width="3" height="5" fill="#fff"/><rect x="8" y="3" width="3" height="7" fill="#fff"/><rect x="12" y="0" width="3" height="10" fill="#fff"/></svg>
      <svg width="14" height="10" viewBox="0 0 14 10"><path d="M1 3.5a9 9 0 0 1 12 0M3.3 5.8a5.5 5.5 0 0 1 7.4 0" stroke="#fff" stroke-width="1.6" fill="none"/><circle cx="7" cy="8.5" r="1.3" fill="#fff"/></svg>
      <svg width="22" height="10" viewBox="0 0 22 10"><rect x="0.5" y="0.5" width="18" height="9" rx="2" stroke="#fff" fill="none"/><rect x="2" y="2" width="15" height="6" rx="1" fill="#fff"/><rect x="19.5" y="3" width="1.5" height="4" fill="#fff"/></svg>
    </span>
  </div>
  <div class="splash-name">Brisko<br>Routine</div>
</section>

<!-- Dashboard screen -->
<section class="screen screen--dashboard">
  <header class="app-header">
    <div class="status-bar">
      <span>9:41</span>
      <span class="status-icons">
        <svg width="16" height="10" viewBox="0 0 16 10"><rect x="0" y="7" width="3" height="3" fill="#fff"/><rect x="4" y="5" width="3" height="5" fill="#fff"/><rect x="8" y="3" width="3" height="7" fill="#fff"/><rect x="12" y="0" width="3" height="10" fill="#fff"/></svg>
        <svg width="14" height="10" viewBox="0 0 14 10"><path d="M1 3.5a9 9 0 0 1 12 0M3.3 5.8a5.5 5.5 0 0 1 7.4 0" stroke="#fff" stroke-width="1.6" fill="none"/><circle cx="7" cy="8.5" r="1.3" fill="#fff"/></svg>
        <svg width="22" height="10" viewBox="0 0 22 10"><rect x="0.5" y="0.5" width="18" height="9" rx="2" stroke="#fff" fill="none"/><rect x="2" y="2" width="15" height="6" rx="1" fill="#fff"/><rect x="19.5" y="3" width="1.5" height="4" fill="#fff"/></svg>
      </span>
    </div>
    <div class="app-header__title">Dashboard</div>
    <svg class="app-header__icon" style="right:14px" width="18" height="18" viewBox="0 0 18 18"><circle cx="7.5" cy="7.5" r="6" stroke="#fff" stroke-width="1.8" fill="none"/><path d="M12 12l5 5" stroke="#fff" stroke-width="1.8"/></svg>
  </header>
  <nav class="tabs">
    <div class="tab tab--active">Workout</div>
    <div class="tab">Calendar</div>
  </nav>
  <div class="card-list">
    <article class="workout-card">
      <div class="workout-card__photo" role="img" aria-label="Close-up photo of a toned abdomen" style="background:linear-gradient(160deg,#6b4a36,#a4745a 45%,#4a3326)"></div>
      <div class="workout-card__caption">
        <div class="workout-card__title">Abs Workout</div>
        <div class="workout-card__desc">Do this quick circuit after cardio (or before the be...</div>
      </div>
    </article>
    <article class="workout-card">
      <div class="workout-card__photo" role="img" aria-label="Photo of legs in running shoes during a lunge" style="background:linear-gradient(150deg,#1d1f22,#3b3e42 50%,#18191b)"></div>
      <div class="workout-card__caption" style="background:transparent">
        <div class="workout-card__title">Leg Workout</div>
        <div class="workout-card__desc">Includes five workout programs to help you build m...</div>
      </div>
    </article>
    <article class="workout-card">
      <div class="workout-card__photo" role="img" aria-label="Photo of a woman stretching on a mat" style="background:linear-gradient(160deg,#8c98a4,#b7aa98 50%,#4f6b82)"></div>
      <div class="workout-card__caption">
        <div class="workout-card__title">Sleepy Time Stretch</div>
        <div class="workout-card__desc">Feel the afterburn all night long with a no-sweat, full-body workout</div>
      </div>
    </article>
    <article class="workout-card workout-card--short">
      <div class="workout-card__photo" role="img" aria-label="Photo of a group exercising together" style="background:linear-gradient(90deg,#7a4a1e,#b9762e 50%,#6b3f18)"></div>
    </article>
  </div>
</section>

<!-- Workout screen -->
<section class="screen screen--workout">
  <header class="app-header">
    <div class="status-bar">
      <span>9:41</span>
      <span class="status-icons">
        <svg width="16" height="10" viewBox="0 0 16 10"><rect x="0" y="7" width="3" height="3" fill="#fff"/><rect x="4" y="5" width="3" height="5" fill="#fff"/><rect x="8" y="3" width="3" height="7" fill="#fff"/><rect x="12" y="0" width="3" height="10" fill="#fff"/></svg>
        <svg width="14" height="10" viewBox="0 0 14 10"><path d="M1 3.5a9 9 0 0 1 12 0M3.3 5.8a5.5 5.5 0 0 1 7.4 0" stroke="#fff" stroke-width="1.6" fill="none"/><circle cx="7" cy="8.5" r="1.3" fill="#fff"/></svg>
        <svg width="22" height="10" viewBox="0 0 22 10"><rect x="0.5" y="0.5" width="18" height="9" rx="2" stroke="#fff" fill="none"/><rect x="2" y="2" width="15" height="6" rx="1" fill="#fff"/><rect x="19.5" y="3" width="1.5" height="4" fill="#fff"/></svg>
      </span>
    </div>
    <svg class="app-header__icon" style="left:14px" width="22" height="16" viewBox="0 0 22 16"><path d="M21 8H2M8 2L2 8l6 6" stroke="#fff" stroke-width="1.8" fill="none"/></svg>
    <div class="app-header__title">Workout</div>
  </header>

  <h2 class="exercise-title">1/15 Jumping Squats</h2>
  <div class="exercise-video" role="img" aria-label="Video still of an instructor demonstrating jumping squats in a studio" style="background:linear-gradient(90deg,#d9d3c6,#c9b9a6 55%,#d4682a 78%,#3d80b8)">
    <svg class="exercise-video__play" width="32" height="32" viewBox="0 0 32 32"><circle cx="16" cy="16" r="14" stroke="#fff" stroke-width="2.5" fill="rgba(0,0,0,.2)"/><path d="M13 10l9 6-9 6z" fill="#fff"/></svg>
  </div>
  <p class="exercise-text">Before any fitness movement or event, you should always properly warm up.</p>
  <p class="exercise-text">You want to start by getting your heart rate up by doing some type of rhythmic movement like jumping jacks or marching in place or light jogging to get your body ready for the upcoming activity.</p>

  <h2 class="exercise-title" style="padding-top:16px">2/15 Reverse Crunches</h2>
  <div class="exercise-video" role="img" aria-label="Video still of a woman doing reverse crunches on a mat" style="background:linear-gradient(160deg,#5a4c3e,#3c4a66 50%,#2e7fa6)">
    <svg class="exercise-video__play" width="32" height="32" viewBox="0 0 32 32"><circle cx="16" cy="16" r="14" stroke="#fff" stroke-width="2.5" fill="rgba(0,0,0,.2)"/><path d="M13 10l9 6-9 6z" fill="#fff"/></svg>
  </div>
  <p class="exercise-text">First, you're going to crunch forward and then</p>

  <div class="fab">
    <svg width="20" height="20" viewBox="0 0 20 20"><path d="M5 2l13 8-13 8z" fill="#1d1d1d"/></svg>
  </div>
</section>

</body>
</html>
```